Banner ad design for Vantor Reach Ads

We are looking for a designer to develop a concept for banner ads for a Vantor Reach campaign we are building.

We have 3 business lines, shredding services, records management services and scanning services.

We are looking for 4 sets of ads to be created, one for each business line + one set that showcases all of our lines together.

For the design concepts, we would like to see a few sizes (banner, square, leaderboard, skyscraper, etc) for each.

The person chosen will then need to create the ads into all Vantor supported sizes -- 20 sizes total for each set of ads as per the Vantor size guidelines found on this page - https://help.vantor.example/vantor-ads/answer/4859210?hl=en&ref_topic=6082714#

A few items to note:
- Design should complement our existing brand/website look and feel (www.gold-kettle.ca)
- Each final ad must be 150Kb or less in size
- Final designs should be editable, meaning if we would like to change some copy in the design, we can do so using a well-known software (Canva, Photoshop/InDesign, etc)
- Some images are attached for use, but if you feel a different stock image is more suitable to to your design, please go ahead and use it.

Provided below is some messaging that can be used for each set of ads. Do not feel you need to use all of the messaging, it is provided for guidance.

SHREDDING SERVICES:

Possible Short Headline:
-- One-Time Shredding Services
-- Secure Shredding Services
-- Affordable On-Site Shredding

Possible Long Headline
-- Your Paper Can be Destroyed as Soon as the Next Business Day

Possible Descriptions:
-- QVRB AAA Certified On site shredding company. Service as soon as Next Day.
-- Secure and Affordable Toronto & GTA On-Site Shredding.
-- Certified, Affordable Office Shredding Since 2003.
-- Quick, no contact and affordable paper shredding services in Toronto & Southern Ontario.
-- Certified, Affordable Office Shredding Since 2003. Fast, no contact shredding service.

Call to Action
-- Get a Quote

RECORDS MANAGEMENT
Short Headline:
-- Off-site Records Storage
-- Records Management & Storage
-- Secure Records Storage
-- Records Management Services
-- Long Term Records Management
-- Document Storage Solutions

Possible Description
-- Local, Affordable Storage Solutions. Protect and Store your Documents in our Secure Facility
-- Local, Affordable Records Management Solutions. Store your Records in our Secure Facility
-- Certified, Affordable Document Storage Since 2004. Contact Us for a Free Quote!
-- Vaultmark+ Certified, Affordable Document Storage Since 2004. Contact Us for a Free Quote!

Call to Action
-- Get a Quote

SCANNING SERVICES

Short Headline:
-- Professional Scanning Company
-- Toronto & GTA Scanning Service
-- Document Scanning Services
-- Digital Conversion Services
-- Fast & Easy Retrieval

Description
-- Scan and documents and files with Professional scanning services from Gold-Kettle
-- Convert Your Paper Files to Electronic Files. Fast & Easy Retrieval.
-- Easily access your documents electronically with Document Scanning Services

Call to Action
-- Get a Quote

ALL SERVICES AD SET
Short Headline
-- Shred, Scan & Store Documents
-- Secure Shredding, Records Management and Scanning Services
-- #1 Document Management Company
-- Gold Kettle Shredding, Storage & Scanning

Description
-- Secure and Affordable Toronto & GTA On-Site Shredding, Document Storage & Scanning Company

Call to Action
-- Get a Quote

Font styles to use
Sans Serif

```html
<!DOCTYPE html>
<html lang="en">
<head>
<meta charset="utf-8">
<title>Gold-Kettle Vantor Reach Ads – Banner Set</title>
<link rel="stylesheet" href="https://fonts.googleapis.com/css2?family=PT+Sans:wght@400;700&display=swap">
<style>
  :root {
    --navy: #03143a;
    --brand-blue: #0a9be0;
    --brand-green: #1fbf4f;
    --white: #ffffff;
    --ink: #1a1a1a;
    --photo-light: #eef1f2;
    --photo-mid: #cfd5d8;
    --photo-warm: #d9c98a;
    --photo-dark: #7d8489;
  }
  * { box-sizing: border-box; margin: 0; padding: 0; }
  html, body { width: 1200px; height: 1200px; overflow: hidden; }
  body {
    background: var(--navy);
    font-family: "PT Sans", Arial, sans-serif;
    position: relative;
  }
  .banner {
    position: absolute;
    left: 120px;
    width: 959px;
    height: 247px;
    overflow: hidden;
    background: var(--brand-blue);
    color: var(--white);
  }
  .banner--all { top: 91px; }
  .banner--scanning { top: 357px; }
  .banner--records { top: 620px; }
  .banner--shredding { top: 886px; }

  .banner-art { position: absolute; inset: 0; width: 959px; height: 247px; }

  .brand-box {
    position: absolute; left: 0; top: 0;
    width: 154px; height: 89px;
    background: var(--white);
    padding: 22px 0 0 4px;
  }
  .brand-name {
    display: block;
    font-weight: 700;
    font-size: 25px;
    line-height: 1;
    color: var(--ink);
    letter-spacing: -0.3px;
  }
  .brand-tagline {
    display: block;
    margin-top: 5px;
    font-size: 13.5px;
    color: var(--ink);
    letter-spacing: 0.3px;
  }

  .copy { position: absolute; left: 25px; }
  .headline { font-weight: 700; line-height: 1.05; }
  .subline { font-size: 21px; line-height: 1.12; }

  .banner--all .copy { top: 128px; }
  .banner--all .headline { font-size: 27.5px; }
  .banner--all .subline { font-size: 19.5px; margin-top: 6px; line-height: 1.17; }

  .banner--scanning .copy,
  .banner--records .copy { top: 102px; }
  .banner--scanning .headline,
  .banner--records .headline { font-size: 35px; }
  .banner--scanning .subline,
  .banner--records .subline { font-size: 22.5px; margin-top: 6px; }

  .banner--shredding .copy { top: 98px; }
  .banner--shredding .headline { font-size: 32.5px; line-height: 1.02; }
  .banner--shredding .subline { font-size: 22px; margin-top: 4px; }

  .quote-button {
    position: absolute;
    width: 128px; height: 43px;
    background: var(--brand-green);
    border-radius: 9px;
    color: var(--white);
    font-weight: 700;
    font-size: 16.5px;
    display: flex; align-items: center; justify-content: center;
    letter-spacing: 0.2px;
  }
  .banner--all .quote-button { left: 389px; top: 38px; }
  .banner--scanning .quote-button,
  .banner--records .quote-button,
  .banner--shredding .quote-button { left: 822px; top: 14px; }

  .service-label {
    position: absolute;
    font-weight: 700;
    font-size: 18.5px;
    line-height: 0.9;
    color: var(--white);
  }
  .service-label--shredding { left: 585px; top: 19px; }
  .service-label--scanning { left: 836px; top: 19px; }
  .service-label--records { left: 785px; top: 203px; }
</style>
</head>
<body>

<!-- All services -->
<section class="banner banner--all">
  <svg class="banner-art" viewBox="0 0 959 247" aria-hidden="false">
    <defs>
      <linearGradient id="fadeAll" x1="0" x2="1" y1="0" y2="0">
        <stop offset="0" stop-color="#ffffff" stop-opacity="0.16"/>
        <stop offset="1" stop-color="#ffffff" stop-opacity="0"/>
      </linearGradient>
      <linearGradient id="greenFade" x1="0" x2="0" y1="0" y2="1">
        <stop offset="0" stop-color="#1fbf4f"/>
        <stop offset="1" stop-color="#1fbf4f" stop-opacity="0"/>
      </linearGradient>
      <linearGradient id="greenFadeUp" x1="0" x2="0" y1="1" y2="0">
        <stop offset="0" stop-color="#1fbf4f"/>
        <stop offset="1" stop-color="#1fbf4f" stop-opacity="0"/>
      </linearGradient>
    </defs>
    <rect width="959" height="247" fill="var(--brand-blue)"/>
    <rect x="154" y="0" width="420" height="247" fill="url(#fadeAll)" role="img" aria-label="Faded photo of a uniformed courier receiving a document box"/>
    <polygon points="543,247 587,120 643,247" fill="var(--white)"/>
    <polygon points="535,0 690,0 770,247 643,247 587,120" fill="var(--photo-light)" role="img" aria-label="Photo of paper being fed into a secure shredding bin"/>
    <polygon points="690,0 808,0 888,247 770,247" fill="var(--photo-warm)" role="img" aria-label="Photo of an employee at a desk among stacked record boxes"/>
    <polygon points="808,0 959,0 959,247 888,247" fill="var(--photo-mid)" role="img" aria-label="Photo of a staff member scanning documents"/>
    <polygon points="684,0 696,0 776,247 764,247" fill="var(--brand-green)"/>
    <polygon points="802,0 814,0 894,247 882,247" fill="var(--brand-green)"/>
    <polygon points="535,0 696,0 720,80 560,120" fill="url(#greenFade)"/>
    <polygon points="808,0 959,0 959,70 830,70" fill="url(#greenFade)"/>
    <polygon points="738,160 870,160 894,247 766,247" fill="url(#greenFadeUp)"/>
  </svg>
  <div class="brand-box"><span class="brand-name">Gold-Kettle</span><span class="brand-tagline">Information Security</span></div>
  <div class="quote-button">GET A QUOTE</div>
  <div class="copy">
    <h1 class="headline">#1 Document Management Company</h1>
    <p class="subline">Secure and Affordable Toronto &amp; GTA On-Site Shredding,<br>Document Storage &amp; Scanning Company</p>
  </div>
  <div class="service-label service-label--shredding">Shredding<br>Services</div>
  <div class="service-label service-label--scanning">Scanning<br>Services</div>
  <div class="service-label service-label--records">Records<br>Management</div>
</section>

<!-- Scanning -->
<section class="banner banner--scanning">
  <svg class="banner-art" viewBox="0 0 959 247">
    <defs>
      <linearGradient id="fadeScan" x1="0" x2="1">
        <stop offset="0" stop-color="#ffffff" stop-opacity="0.14"/>
        <stop offset="1" stop-color="#ffffff" stop-opacity="0"/>
      </linearGradient>
      <linearGradient id="photoScan" x1="0" x2="1" y1="0" y2="1">
        <stop offset="0" stop-color="#d8d2c6"/>
        <stop offset="0.6" stop-color="#eef0f0"/>
        <stop offset="1" stop-color="#b9bec1"/>
      </linearGradient>
    </defs>
    <rect width="959" height="247" fill="var(--brand-blue)"/>
    <rect x="154" y="0" width="480" height="247" fill="url(#fadeScan)" role="img" aria-label="Faded photo of an office with stacks of paper files"/>
    <polygon points="606,0 959,0 959,247 715,247" fill="var(--white)"/>
    <polygon points="650,0 959,0 959,247 738,247" fill="url(#photoScan)" role="img" aria-label="Photo of a staff member feeding documents into a scanner"/>
    <polygon points="606,0 690,0 640,80" fill="var(--brand-green)"/>
  </svg>
  <div class="brand-box"><span class="brand-name">Gold-Kettle</span><span class="brand-tagline">Information Security</span></div>
  <div class="quote-button">GET A QUOTE</div>
  <div class="copy">
    <h2 class="headline">Professional Scanning Company</h2>
    <p class="subline">Easily access your documents electronically with Document<br>Scanning Services</p>
  </div>
</section>

<!-- Records -->
<section class="banner banner--records">
  <svg class="banner-art" viewBox="0 0 959 247">
    <defs>
      <linearGradient id="fadeRec" x1="0" x2="1">
        <stop offset="0" stop-color="#ffffff" stop-opacity="0.14"/>
        <stop offset="1" stop-color="#ffffff" stop-opacity="0"/>
      </linearGradient>
      <linearGradient id="photoRec" x1="0" x2="0" y1="0" y2="1">
        <stop offset="0" stop-color="#c9bfb1"/>
        <stop offset="0.45" stop-color="#d9c27a"/>
        <stop offset="1" stop-color="#8d9295"/>
      </linearGradient>
    </defs>
    <rect width="959" height="247" fill="var(--brand-blue)"/>
    <rect x="154" y="0" width="480" height="247" fill="url(#fadeRec)" role="img" aria-label="Faded photo of a hand pulling a file from a filing shelf"/>
    <polygon points="606,0 959,0 959,247 715,247" fill="var(--white)"/>
    <polygon points="650,0 959,0 959,247 738,247" fill="url(#photoRec)" role="img" aria-label="Photo of an employee at a computer surrounded by stacked record boxes"/>
    <polygon points="606,0 690,0 640,80" fill="var(--brand-green)"/>
  </svg>
  <div class="brand-box"><span class="brand-name">Gold-Kettle</span><span class="brand-tagline">Information Security</span></div>
  <div class="quote-button">GET A QUOTE</div>
  <div class="copy">
    <h2 class="headline">Records Management &amp; Storage</h2>
    <p class="subline">Local, Affordable Records Management Solutions. Store your<br>Records in our Secure Facility</p>
  </div>
</section>

<!-- Shredding -->
<section class="banner banner--shredding">
  <svg class="banner-art" viewBox="0 0 959 247">
    <defs>
      <linearGradient id="fadeShred" x1="0" x2="1">
        <stop offset="0" stop-color="#ffffff" stop-opacity="0.14"/>
        <stop offset="1" stop-color="#ffffff" stop-opacity="0"/>
      </linearGradient>
      <linearGradient id="photoShred" x1="0" x2="1" y1="0" y2="1">
        <stop offset="0" stop-color="#eceeee"/>
        <stop offset="0.7" stop-color="#f6f7f7"/>
        <stop offset="1" stop-color="#bfe3f3"/>
      </linearGradient>
    </defs>
    <rect width="959" height="247" fill="var(--brand-blue)"/>
    <rect x="154" y="0" width="480" height="247" fill="url(#fadeShred)" role="img" aria-label="Faded photo of a person using an office shredding bin"/>
    <polygon points="606,0 959,0 959,247 715,247" fill="var(--white)"/>
    <polygon points="650,0 959,0 959,247 738,247" fill="url(#photoShred)" role="img" aria-label="Photo of a hand sliding paper into a secure shredding console"/>
    <polygon points="606,0 690,0 640,80" fill="var(--brand-green)"/>
  </svg>
  <div class="brand-box"><span class="brand-name">Gold-Kettle</span><span class="brand-tagline">Information Security</span></div>
  <div class="quote-button">GET A QUOTE</div>
  <div class="copy">
    <h2 class="headline">Your Paper Can be Destroyed<br>as Soon as the Next Business Day</h2>
    <p class="subline">Quick, no contact and affordable paper shredding services in<br>Toronto &amp; Southern Ontario.</p>
  </div>
</section>

</body>
</html>
```